BLUE HAVEN (Business Card for Training Company)

Blue Haven is a training and consultancy company with a focus on executive protection and medical. I would like the card to be nice and sharp, not overdone and in black and red. I would also like it to highlight that it is "A Dravin Company"

I would like it to be simple and highlight a few things.

1. Name
2. Title
3. Phone Number
4. Email

I would also like www.dravinholdings.example/blue-haven to be on the card somewhere.

Target Market(s)

Security Companies

Industry/Entity Type

Security

Contact Information for Business Card

Blue Haven is a training and consultancy company with a focus on executive protection and medical. I would like the card to be nice and sharp, not overdone and in black and red. I would also like it to highlight that it is "A Dravin Company" I would like it to be simple and highlight a few things. 1. Name 2. Title 3. Phone Number 4. Email I would also like www.dravinholdings.example/blue-haven to be on the card somewhere.

Requirements
Must have
• A Dravin Company listed on the card and the website
Nice to have
• Highlight Medical Training, Consultancy & Executive Protection Courses

```html
<!DOCTYPE html>
<html lang="en">
<head>
<meta charset="utf-8">
<title>Blue Haven — Business Card</title>
<link href="https://fonts.googleapis.com/css2?family=Open+Sans:wght@400;600;800&display=swap" rel="stylesheet">
<style>
  :root {
    --page: #e9e7e3;
    --card: #ffffff;
    --maroon: #650000;
    --ink: #000000;
    --logo-ink: #111111;
    --type-light: #ffffff;
    --type-dark: #333333;
  }
  * { margin: 0; padding: 0; box-sizing: border-box; }
  html, body { width: 900px; height: 1200px; overflow: hidden; }
  body {
    background: var(--page);
    font-family: "Open Sans", "Carlito", sans-serif;
    position: relative;
  }
  .card {
    position: absolute;
    width: 734px;
    height: 428px;
    border-radius: 27px;
    background: var(--card);
    overflow: hidden;
    box-shadow: 0 4px 14px rgba(0,0,0,0.18);
  }
  .card--front { left: 80px; top: 128px; }
  .card--back  { left: 79px; top: 645px; width: 732px; height: 430px; }

  .card__bands { position: absolute; inset: 0; width: 100%; height: 100%; }

  .brand {
    position: absolute;
    left: 0;
    width: 100%;
    display: flex;
    flex-direction: column;
    align-items: center;
  }
  .card--front .brand { top: 66px; }
  .card--back .brand  { top: 150px; }

  .wordmark {
    font-weight: 800;
    font-size: 62px;
    line-height: 0.95;
    letter-spacing: 0.01em;
    color: var(--logo-ink);
    text-align: left;
  }
  .parent-line {
    margin-top: 10px;
    font-size: 14px;
    font-weight: 600;
    letter-spacing: 0.28em;
    text-transform: uppercase;
    color: var(--maroon);
  }

  .contact {
    position: absolute;
    left: 122px;
    color: var(--type-light);
    font-size: 15.5px;
    line-height: 1;
    display: flex;
    align-items: center;
    white-space: nowrap;
  }
  .contact--person  { top: 300px; font-weight: 600; font-size: 16px; }
  .contact--address { top: 325px; }
  .contact--lines   { top: 349px; }
  .contact__title { font-weight: 400; margin-left: 8px; padding-left: 8px; border-left: 1px solid var(--type-light); }
  .contact svg { fill: var(--type-light); flex: none; }
  .contact .icon { margin-right: 8px; }
  .contact .icon--inline { margin: 0 5px 0 4px; }

  .website {
    position: absolute;
    top: 366px;
    left: 0;
    width: 100%;
    text-align: center;
    font-size: 18px;
    letter-spacing: 0.2em;
    color: var(--type-dark);
  }
</style>
</head>
<body>

<section class="card card--front" aria-label="Card front">
  <svg class="card__bands" viewBox="0 0 734 428" preserveAspectRatio="none" aria-hidden="true">
    <path d="M0 293 Q367 200 734 296 L734 428 L0 428 Z" fill="var(--ink)"/>
    <path d="M0 315 Q367 210 734 313 L734 428 L0 428 Z" fill="var(--card)"/>
    <path d="M0 331 Q367 180 734 331 L734 428 L0 428 Z" fill="var(--maroon)"/>
    <path d="M120 428 Q367 372 612 428 Z" fill="var(--card)"/>
    <path d="M180 428 Q367 390 555 428 Z" fill="var(--ink)"/>
  </svg>

  <div class="brand">
    <div class="wordmark">BLUE<br>HAVEN</div>
    <p class="parent-line">A Dravin Company</p>
  </div>

  <p class="contact contact--person">
    John Morgan<span class="contact__title">Lead Instructor</span>
  </p>
  <p class="contact contact--address">
    <svg class="icon" width="12" height="15" viewBox="0 0 12 15"><path d="M6 0a6 6 0 0 0-6 6c0 4 6 9 6 9s6-5 6-9a6 6 0 0 0-6-6zm0 8.3A2.3 2.3 0 1 1 6 3.7a2.3 2.3 0 0 1 0 4.6z"/></svg>
    418 Harlow Street NW Suite 210. Brookfield MI 49321
  </p>
  <p class="contact contact--lines">
    <svg class="icon" width="15" height="15" viewBox="0 0 24 24"><path d="M6.6 10.8a15 15 0 0 0 6.6 6.6l2.2-2.2c.3-.3.7-.4 1-.2 1.1.4 2.3.6 3.6.6.6 0 1 .4 1 1V20c0 .6-.4 1-1 1A17 17 0 0 1 3 4c0-.6.4-1 1-1h3.5c.6 0 1 .4 1 1 0 1.3.2 2.5.6 3.6.1.3 0 .7-.2 1z"/></svg>
    555-014-7721
    <svg class="icon--inline" width="14" height="14" viewBox="0 0 24 24"><path d="M6 2h12v5H6zM3 8h18a2 2 0 0 1 2 2v7h-4v5H5v-5H1v-7a2 2 0 0 1 2-2zm4 9v3h10v-6H7z"/></svg>
    555-014-7721
    <svg class="icon--inline" width="12" height="9" viewBox="0 0 24 18"><path d="M0 0h24v18H0zM2 2v1l10 7 10-7V2zm0 4v10h20V6l-10 7z"/></svg>
    jmorgan@bluehaven.example
  </p>
</section>

<section class="card card--back" aria-label="Card back">
  <div class="brand">
    <div class="wordmark">BLUE<br>HAVEN</div>
    <p class="parent-line">A Dravin Company</p>
  </div>
  <p class="website">www.dravinholdings.example/blue-haven</p>
</section>

</body>
</html>
```